Cover for a thriller parody: "Until the Pelicans dance"

Creation of a cover for the book "Until the pelicans dance". The text is a parody of the Belmonte Fargas thrillers: humor and colorful characters! So the cover must be parodic, funny, humorous. The joined file is an example of cover with an ostrich (from the title). It's only a draft to show that the Ostrich should look ironic or funny.
Target Market(s)
General public
Industry/Entity Type
Book Publisher
Colors
Designer to choose colors to be used in the design.
Requirements
Must have
- AUTHOR: Luc-Étienne Varoquier
TITLE: Until the pelicans dance (= “until the Pelicans dance”)
PUBLISHER: Editions Norvelle (at the bottom of the page)

```html
<!DOCTYPE html>
<html lang="en">
<head>
<meta charset="utf-8">
<title>Until the Pelicans dance — Cover</title>
<link rel="stylesheet" href="https://fonts.googleapis.com/css2?family=Gelasio:wght@500&family=Stardos+Stencil:wght@700&family=Noto+Sans:wght@400&display=swap">
<style>
  :root {
    --stage: #6f6f6f;
    --paper: #ffffff;
    --paper-shade: #f2f2f2;
    --title-ink: #1f3234;
    --author-ink: #2b3a1f;
    --publisher-ink: #1a1a1a;
    --bird-light: #d4d4d4;
    --bird-dark: #2a2a2a;
  }
  * { margin: 0; padding: 0; box-sizing: border-box; }
  html, body {
    width: 1200px;
    height: 800px;
    overflow: hidden;
    background: var(--stage);
  }
  .stage {
    position: relative;
    width: 1200px;
    height: 800px;
    display: flex;
    align-items: center;
    justify-content: center;
  }
  .cover {
    position: relative;
    width: 470px;
    height: 760px;
    background: linear-gradient(180deg, var(--paper) 0%, var(--paper) 70%, var(--paper-shade) 100%);
    overflow: hidden;
  }
  .cover__author {
    position: absolute;
    top: 52px;
    left: 0;
    width: 100%;
    text-align: center;
    font-family: "Gelasio", Georgia, serif;
    font-weight: 500;
    font-size: 31px;
    color: var(--author-ink);
  }
  .cover__mascot {
    position: absolute;
    top: 130px;
    left: 286px;
    width: 150px;
    height: 268px;
  }
  .cover__title {
    position: absolute;
    top: 222px;
    left: 44px;
    font-family: "Stardos Stencil", "Stencil", serif;
    font-weight: 700;
    color: var(--title-ink);
    text-transform: uppercase;
  }
  .cover__title-line { display: block; line-height: 1; }
  .cover__title-line--until { font-size: 70px; height: 70px; }
  .cover__title-line--the { font-size: 74px; height: 74px; margin-top: 18px; }
  .cover__title-line--pelicans { font-size: 64px; height: 64px; margin-top: 32px; }
  .cover__title-line--dance { font-size: 96px; height: 96px; margin-top: 4px; }
  .cover__publisher {
    position: absolute;
    bottom: 40px;
    left: 0;
    width: 100%;
    text-align: center;
    font-family: "Noto Sans", Arial, sans-serif;
    font-size: 20px;
    letter-spacing: 1.5px;
    color: var(--publisher-ink);
  }
</style>
</head>
<body>
  <main class="stage">
    <article class="cover">
      <p class="cover__author">Luc-Étienne Varoquier</p>

      <svg class="cover__mascot" viewBox="0 0 150 268" role="img" aria-label="Cartoon illustration of a funny long-necked bird sitting and looking at the reader">
        <defs>
          <linearGradient id="mascot-tone" x1="0" y1="0" x2="0" y2="1">
            <stop offset="0" stop-color="var(--bird-light)"/>
            <stop offset="1" stop-color="var(--bird-dark)"/>
          </linearGradient>
        </defs>
        <rect x="0" y="0" width="150" height="268" rx="10" fill="url(#mascot-tone)"/>
      </svg>

      <h1 class="cover__title">
        <span class="cover__title-line cover__title-line--until">Until</span>
        <span class="cover__title-line cover__title-line--the">the</span>
        <span class="cover__title-line cover__title-line--pelicans">Pelicans</span>
        <span class="cover__title-line cover__title-line--dance">Dance</span>
      </h1>

      <p class="cover__publisher">Editions Norvelle</p>
    </article>
  </main>
</body>
</html>
```